Tidal Quill is a premium Spa and Salon only professional tanning brand.

We need a email template/newsletter that we can send to our client base any time we would like to share information with them.
Whether this is launching our Christmas gift, or sharing up and coming training dates it will be another avenue for us to stay in touch with our clients.
We like to think ourselves as the 'Verrington handbag' in the tanning world, Tidal Quill is a brand that is desirable and exclusive and has people hooked once they trial the brand and are blown away by the results.
www.tidal-quill-example.com

```html
<!DOCTYPE html>
<html lang="en">
<head>
<meta charset="utf-8">
<title>Tidal Quill Newsletter</title>
<link href="https://fonts.googleapis.com/css2?family=Noto+Serif:wght@400;700&family=Arimo:wght@400;700&display=swap" rel="stylesheet">
<style>
  :root {
    --brand-brown: #8b5433;
    --text-brown: #5b3a2a;
    --heading-blue: #1b5a8c;
    --link-blue: #1d6ba8;
    --frame-top: #c9eefa;
    --frame-bottom: #1a74b8;
    --button-top: #3d9bd8;
    --button-bottom: #0f5d9a;
    --shade-light: #e3c39a;
    --shade-medium: #a9703f;
    --shade-dark: #7a2f12;
    --panel: #ffffff;
    --serif: "Noto Serif", Georgia, serif;
    --sans: "Arimo", Arial, sans-serif;
  }
  * { box-sizing: border-box; margin: 0; padding: 0; }
  html, body { width: 746px; height: 1200px; overflow: hidden; background: #fff; }
  .newsletter { position: relative; width: 746px; height: 1200px; font-family: var(--serif); color: var(--text-brown); }

  .brand-name { position: absolute; left: 26px; top: 4px; font-family: var(--serif); font-weight: 700; color: var(--brand-brown); font-size: 78px; line-height: 80px; letter-spacing: 1px; }
  .site-url { position: absolute; right: 25px; top: 147px; font-family: var(--sans); font-weight: 700; font-size: 20px; color: var(--link-blue); text-decoration: none; }

  .frame { position: absolute; left: 24px; top: 181px; width: 697px; height: 837px; background: linear-gradient(to bottom, var(--frame-top), var(--frame-bottom)); }
  .panel { position: absolute; left: 19px; top: 24px; width: 658px; height: 790px; background: var(--panel); overflow: hidden; }

  .backdrop { position: absolute; left: 0; top: 300px; width: 380px; height: 490px; background: radial-gradient(ellipse at 45% 45%, rgba(232,205,180,0.35), rgba(255,255,255,0) 70%); }

  .headline { position: absolute; right: 16px; top: 57px; text-align: right; font-weight: 700; color: var(--heading-blue); font-size: 25px; line-height: 27px; white-space: nowrap; }

  .thumb { position: absolute; left: 25px; top: 123px; width: 162px; height: 138px; background: linear-gradient(135deg, #f3e6d8, #d9b58e 60%, #f6efe6); }

  .intro { position: absolute; left: 204px; top: 134px; width: 434px; font-size: 17px; line-height: 23px; text-align: justify; }
  .intro strong { color: var(--heading-blue); }

  .shades { position: absolute; left: 23px; top: 285px; width: 165px; }
  .shade { height: 14px; margin-bottom: 13px; }
  .shade.light { background: var(--shade-light); }
  .shade.medium { background: var(--shade-medium); }
  .shade.dark { background: var(--shade-dark); }

  .timing { position: absolute; left: 204px; top: 258px; font-size: 17px; line-height: 23px; }
  .timing ul { margin-top: 3px; padding-left: 30px; }

  .choose { position: absolute; left: 204px; top: 380px; font-size: 19px; line-height: 24px; font-weight: 700; color: var(--heading-blue); }

  .read-more { position: absolute; display: block; width: 106px; height: 30px; border-radius: 6px; background: linear-gradient(to bottom, var(--button-top), var(--button-bottom)); color: #fff; font-family: var(--serif); font-size: 15px; line-height: 30px; text-align: center; text-decoration: none; box-shadow: 0 1px 3px rgba(0,0,0,0.35); }
  .read-more.first { left: 204px; top: 430px; }
  .read-more.second { left: 23px; top: 726px; }

  .feature-title { position: absolute; left: 23px; top: 506px; width: 320px; font-size: 29px; line-height: 31px; font-weight: 700; color: var(--heading-blue); }
  .feature-copy { position: absolute; left: 23px; top: 578px; width: 324px; font-size: 17px; line-height: 23px; text-align: justify; }
  .feature-copy strong { color: var(--heading-blue); letter-spacing: 1.5px; }

  .product-ring { position: absolute; left: 383px; top: 484px; width: 270px; height: 270px; }
  .product-shot { position: absolute; left: 411px; top: 511px; width: 197px; height: 227px; background: linear-gradient(to right, #f4f1ee, #e8dccd 50%, #d8c0a2); border-radius: 6px; }
  .seal { position: absolute; left: 546px; top: 485px; width: 78px; height: 78px; border-radius: 50%; background: var(--brand-brown); }

  .footer-icon { position: absolute; top: 1030px; width: 72px; height: 72px; }
  .footer-icon.mail { left: 68px; }
  .footer-icon.social { left: 164px; }

  .address { position: absolute; left: 282px; top: 1049px; width: 180px; text-align: center; font-size: 10px; line-height: 13px; color: #222; }
  .address .company { font-weight: 700; margin-bottom: 5px; }

  .badge { position: absolute; border-radius: 50%; }
  .badge.cruelty-free { left: 501px; top: 1040px; width: 67px; height: 62px; border-radius: 12px; background: #9a6038; }
  .badge.organic { left: 609px; top: 1039px; width: 69px; height: 69px; background: var(--brand-brown); }

  .footer-links { position: absolute; left: 0; top: 1139px; width: 746px; text-align: center; font-family: var(--sans); font-size: 19px; line-height: 24px; color: var(--link-blue); }
  .footer-links a { color: var(--link-blue); text-decoration: none; }
</style>
</head>
<body>
<main class="newsletter">
  <header>
    <div class="brand-name">Tidal<br>Quill</div>
    <a class="site-url" href="#">www.tidal-quill-example.com</a>
  </header>

  <section class="frame">
    <div class="panel">
      <div class="backdrop" role="img" aria-label="Faint photo of a woman relaxing with autumn leaves"></div>

      <h1 class="headline">Great news!<br>The 2-6 hour tanning&nbsp; revolution has arrived!</h1>

      <div class="thumb" role="img" aria-label="Campaign image of tanned legs with falling autumn leaves"></div>

      <p class="intro">This revolutionary new rapid tanning product takes just <strong>2-6 hours to develop</strong>, and allows you to control the depth of your tan by choosing for yourself when to shower it off.</p>

      <div class="shades">
        <div class="shade light"></div>
        <div class="shade medium"></div>
        <div class="shade dark"></div>
      </div>

      <div class="timing">
        <p>Showering times to achieve your desired colour:</p>
        <ul>
          <li>Light - Shower at 2 hours</li>
          <li>Medium - Shower at 4 hours</li>
          <li>Dark - Shower at 6 hours</li>
        </ul>
      </div>

      <p class="choose">Now you can choose your colour!</p>
      <a class="read-more first" href="#">READ MORE</a>

      <h2 class="feature-title">A revolution in self tanning</h2>
      <p class="feature-copy">Tidal Quill has been developed with a <strong>unique organic formula</strong>, enriched with <strong>deep moisturisers</strong> and <strong>free from paraben and alcohol</strong>, ensuring a streak-free, soft finish.</p>
      <a class="read-more second" href="#">READ MORE</a>

      <svg class="product-ring" viewBox="0 0 270 270" aria-hidden="true">
        <defs>
          <linearGradient id="ringShade" x1="0" y1="0" x2="0" y2="1">
            <stop offset="0" stop-color="#bfeaf8"/>
            <stop offset="1" stop-color="#1a74b8"/>
          </linearGradient>
        </defs>
        <circle cx="135" cy="135" r="128" fill="#fff" stroke="url(#ringShade)" stroke-width="12"/>
      </svg>
      <div class="product-shot" role="img" aria-label="Three white tanning product bottles"></div>
      <div class="seal" role="img" aria-label="Organic certification badge"></div>
    </div>
  </section>

  <footer>
    <svg class="footer-icon mail" viewBox="0 0 72 72" role="img" aria-label="Email">
      <circle cx="36" cy="36" r="36" fill="#8b5433"/>
      <rect x="15" y="22" width="42" height="28" fill="none" stroke="#fff" stroke-width="3"/>
      <polyline points="15,22 36,40 57,22" fill="none" stroke="#fff" stroke-width="3"/>
    </svg>
    <svg class="footer-icon social" viewBox="0 0 72 72" role="img" aria-label="Social page">
      <circle cx="36" cy="36" r="36" fill="#8b5433"/>
    </svg>

    <div class="address">
      <p class="company">Tidal Quill</p>
      <p>Harbourline Business Centre</p>
      <p>Meadowgate Road Trade Park</p>
      <p>Oakridge, County Fennel OK14 7QZ</p>
    </div>

    <div class="badge cruelty-free" role="img" aria-label="Not tested on animals badge"></div>
    <div class="badge organic" role="img" aria-label="Organic badge"></div>

    <p class="footer-links"><a href="#">unsubscribe from this list</a>&nbsp; | &nbsp;<a href="#">view email in browser</a></p>
  </footer>
</main>
</body>
</html>
```